Business card design for a dynamic IT consulting company

We need a business card design for a young firm, specialized in the Telecommunications/Consulting industry. The name of the company is Brask and Partners Business Consulting Ltd. (Short name: Brask and Partnes)
Brask = solve read reverse, so we aim to be uncomplicated and solution-oriented. The small pipe in our logo is also related to the word solve. So we need a new business card design, which is simple, eye catching and something non traditional (I would probably prefer a square shaped design rather than a rectangle, but open for suggestions). Attached our logo.

Target Market(s)

Usually our customers are Tier1 Telecoms providers (Q-Linkra, Parnexo, etc) and their executives.

Industry/Entity Type

Business

Contact Information for Business Card

Name: Gergely Halmindo
Email: g.halmindo@braskpartnera.hu
Web: www.braskpartnera.hu
Mobile: +36 30 555 0192
Title: Managing Director

Optional:
Company name: Brask and Partners Ltd.
Address: 1047 Budapest, Ravaszi str. 17/B, Hungary

Font styles to use
Other font styles liked:
• helveticaneue_medium, Prime Regular are used now.

Colors

Designer to choose colors to be used in the design.

Requirements
Must have
• I would like to have a 2 sided design.
Nice to have
• I thought if we make the logo a bit bigger (without the company name), that could go to the back with the company name below. I though, if the pipe in the logo is somehow touchable on the business card, would be nice and unique.

```html
<!DOCTYPE html>
<html lang="en">
<head>
<meta charset="utf-8">
<title>Brask &amp; Partners – Business Card</title>
<link href="https://fonts.googleapis.com/css2?family=Jura:wght@500;600&family=Inter:wght@400&display=swap" rel="stylesheet">
<style>
  :root {
    --stage: #e6e6ea;
    --card-dark: #1b1b1d;
    --card-dark-edge: #2a2a2d;
    --card-light: #ffffff;
    --silver: #c9c9cc;
    --grey-text: #6d6d72;
    --ink: #222226;
    --cyan: #23a6d8;
    --magenta: #c0309a;
    --bar-grey: #8a8a8e;
  }
  * { box-sizing: border-box; margin: 0; padding: 0; }
  html, body { width: 1200px; height: 900px; overflow: hidden; }
  body {
    background: var(--stage);
    font-family: "Inter", "Helvetica Neue", Arial, sans-serif;
    position: relative;
  }
  .card {
    position: absolute;
    top: 200px;
    width: 500px;
    height: 500px;
    border-radius: 28px;
    overflow: hidden;
    box-shadow: 0 14px 30px rgba(0,0,0,.18);
  }

  /* Front side */
  .card--front {
    left: 70px;
    background: var(--card-dark);
  }
  .card--front .texture {
    position: absolute;
    inset: 0;
    background: radial-gradient(circle at 60% 35%, var(--card-dark-edge), var(--card-dark) 70%);
  }
  .card--front .brand {
    position: absolute;
    left: 0; right: 0;
    top: 318px;
    text-align: center;
    font-family: "Jura", "Helvetica Neue", sans-serif;
    font-weight: 500;
    font-size: 52px;
    letter-spacing: .5px;
    color: var(--silver);
  }
  .card--front .url {
    position: absolute;
    left: 0; right: 0;
    top: 400px;
    text-align: center;
    font-family: "Jura", "Helvetica Neue", sans-serif;
    font-weight: 600;
    font-size: 19px;
    letter-spacing: 5px;
    color: var(--silver);
  }

  /* Back side */
  .card--back {
    left: 630px;
    background: var(--card-light);
  }
  .edge-bar {
    position: absolute;
    left: 0;
    width: 9px;
  }
  .edge-bar--grey { top: 70px; height: 75px; background: var(--bar-grey); }
  .edge-bar--cyan { top: 160px; height: 70px; background: var(--cyan); }
  .edge-bar--magenta { top: 250px; height: 120px; background: var(--magenta); }

  .person {
    position: absolute;
    left: 42px;
    top: 72px;
    font-family: "Jura", "Helvetica Neue", sans-serif;
    font-weight: 600;
    font-size: 28px;
  }
  .person .given { color: var(--cyan); }
  .person .family { color: var(--magenta); }
  .role {
    position: absolute;
    left: 42px;
    top: 113px;
    font-size: 19px;
    color: var(--grey-text);
  }
  .contact {
    position: absolute;
    left: 42px;
    list-style: none;
    font-size: 17.5px;
    color: var(--ink);
    line-height: 27px;
  }
  .contact li { display: flex; align-items: flex-start; }
  .contact svg { width: 16px; height: 16px; margin: 5px 10px 0 0; flex: none; fill: var(--ink); }
  .contact--address { top: 160px; }
  .contact--lines { top: 233px; }

  .back-brand {
    position: absolute;
    right: 30px;
    bottom: 52px;
    display: flex;
    align-items: center;
    gap: 12px;
  }
  .back-brand .dot {
    width: 12px; height: 12px;
    background: var(--magenta);
  }
  .back-brand .name {
    font-family: "Jura", "Helvetica Neue", sans-serif;
    font-weight: 500;
    font-size: 32px;
    color: var(--grey-text);
  }
</style>
</head>
<body>

<section class="card card--front" aria-label="Card front">
  <div class="texture" role="img" aria-label="Dark embossed surface area"></div>
  <div class="brand">Brask &amp; Partners</div>
  <div class="url">www.braskpartnera.hu</div>
</section>

<section class="card card--back" aria-label="Card back">
  <span class="edge-bar edge-bar--grey"></span>
  <span class="edge-bar edge-bar--cyan"></span>
  <span class="edge-bar edge-bar--magenta"></span>

  <h1 class="person"><span class="given">Gergely</span> <span class="family">Halmindo</span></h1>
  <p class="role">Managing Director</p>

  <ul class="contact contact--address">
    <li>
      <svg viewBox="0 0 16 16"><path d="M8 0a5.5 5.5 0 0 0-5.5 5.5C2.5 10 8 16 8 16s5.5-6 5.5-10.5A5.5 5.5 0 0 0 8 0zm0 8a2.5 2.5 0 1 1 0-5 2.5 2.5 0 0 1 0 5z"/></svg>
      <span>1047 Budapest<br>Ravaszi str. 17/B, Hungary</span>
    </li>
  </ul>

  <ul class="contact contact--lines">
    <li>
      <svg viewBox="0 0 16 16"><path d="M3.6 1.2l2.2 2.7c.3.4.3.9 0 1.3L4.7 6.5c.9 2 2.6 3.7 4.8 4.8l1.3-1.1c.4-.3.9-.3 1.3 0l2.7 2.2c.4.3.4.9.1 1.3l-1.3 1.5c-.5.6-1.3.8-2 .5C6.3 14 2 9.7.3 4.4c-.2-.7 0-1.5.5-2L2.3 1c.4-.3 1-.3 1.3.2z"/></svg>
      <span>+ 36 30 555 0478</span>
    </li>
    <li>
      <svg viewBox="0 0 16 16"><path d="M4.5 0h7A1.5 1.5 0 0 1 13 1.5v13a1.5 1.5 0 0 1-1.5 1.5h-7A1.5 1.5 0 0 1 3 14.5v-13A1.5 1.5 0 0 1 4.5 0zM4.5 1.5v11h7v-11zM8 13.3a.8.8 0 1 0 0 1.6.8.8 0 0 0 0-1.6z"/></svg>
      <span>+ 36 30 555 0192</span>
    </li>
    <li>
      <svg viewBox="0 0 16 16"><path d="M1 3h14v10H1zm1.6 1.4L8 8.6l5.4-4.2zM2.3 5.4v6.3h11.4V5.4L8 9.9z"/></svg>
      <span>g.halmindo@braskpartnera.hu</span>
    </li>
    <li>
      <svg viewBox="0 0 16 16"><path d="M8 .5a7.5 7.5 0 1 0 0 15 7.5 7.5 0 0 0 0-15zm5.9 6.8h-2.8a11 11 0 0 0-1.2-5A6.1 6.1 0 0 1 13.9 7.3zM8 1.9c.8 1 1.6 2.9 1.7 5.4H6.3C6.4 4.8 7.2 2.9 8 1.9zm-1.9.4a11 11 0 0 0-1.2 5H2.1A6.1 6.1 0 0 1 6.1 2.3zM2.1 8.7h2.8a11 11 0 0 0 1.2 5 6.1 6.1 0 0 1-4-5zM8 14.1c-.8-1-1.6-2.9-1.7-5.4h3.4c-.1 2.5-.9 4.4-1.7 5.4zm1.9-.4a11 11 0 0 0 1.2-5h2.8a6.1 6.1 0 0 1-4 5z"/></svg>
      <span>www.braskpartnera.hu</span>
    </li>
  </ul>

  <div class="back-brand">
    <span class="dot"></span>
    <span class="name">Brask &amp; Partners</span>
  </div>
</section>

</body>
</html>
```